Design some Business Cards for Quizwell

I would like to have a business card designed.

Use the logo from https://www.quizwell-demo.net - we're an education company, keep it elegant and simple; nothing too extravagant. Double Sided isn't necessary but could be better.

Name: Dov Renkel, Founder
Email: dov@quizwell-demo.net
Phone: 5550142986
website: https://www.quizwell-demo.net

Would like the slogan "Exam Management Made Easy" on the back if possible.

```html
<!DOCTYPE html>
<html lang="en">
<head>
<meta charset="utf-8">
<title>Quizwell Business Card</title>
<link href="https://fonts.googleapis.com/css2?family=Lato:wght@400;700;900&display=swap" rel="stylesheet">
<style>
  :root {
    --page-bg: #e9e7e3;
    --card-bg: #252633;
    --accent: #6cb33f;
    --text-light: #f2f2f2;
    --text-muted: #9a9ca6;
  }
  * { box-sizing: border-box; margin: 0; padding: 0; }
  html, body {
    width: 1200px; height: 841px; overflow: hidden;
    background: var(--page-bg);
    font-family: "Lato", Arial, sans-serif;
  }
  .sheet {
    width: 1200px; height: 841px;
    display: flex; flex-direction: column;
    align-items: center; justify-content: center; gap: 40px;
  }
  .card {
    position: relative;
    width: 640px; height: 366px;
    background: var(--card-bg);
    border-radius: 6px;
    box-shadow: 0 8px 22px rgba(0,0,0,0.22);
    color: var(--text-light);
    overflow: hidden;
  }
  .wordmark {
    font-weight: 900; color: var(--text-light);
    letter-spacing: 0.5px; line-height: 1;
  }
  /* front */
  .card-front .wordmark { position: absolute; right: 50px; top: 50px; font-size: 38px; }
  .divider {
    position: absolute; left: 38px; right: 50px; top: 94px;
    height: 2px; background: var(--accent);
  }
  .identity-name {
    position: absolute; left: 38px; top: 62px;
    font-size: 25px; font-weight: 400; line-height: 1.1;
  }
  .identity-role {
    position: absolute; left: 86px; top: 101px;
    font-size: 18px; color: var(--text-muted); font-weight: 400; line-height: 1.1;
  }
  .contact-list {
    position: absolute; left: 38px; bottom: 40px;
    list-style: none; display: flex; flex-direction: column; gap: 9px;
  }
  .contact-item { display: flex; align-items: center; gap: 16px; font-size: 16px; }
  .contact-icon {
    width: 62px; height: 26px; background: var(--accent);
    display: flex; align-items: center; justify-content: center;
  }
  .contact-icon svg { width: 16px; height: 16px; }
  /* back */
  .card-back { display: flex; align-items: center; justify-content: center; }
  .back-lockup { display: flex; flex-direction: column; align-items: center; gap: 10px; }
  .card-back .wordmark { font-size: 50px; }
  .slogan { font-size: 19px; color: var(--text-light); }
  .website { font-size: 15px; color: var(--text-muted); margin-top: 6px; }
</style>
</head>
<body>
<main class="sheet">
  <section class="card card-front" aria-label="Card front">
    <div class="wordmark">Quizwell</div>
    <div class="divider"></div>
    <p class="identity-name">Dov Renkel</p>
    <p class="identity-role">Founder</p>
    <ul class="contact-list">
      <li class="contact-item">
        <span class="contact-icon">
          <svg viewBox="0 0 16 16"><path fill="#fff" d="M3.5 1.5l2.5 2.6-1.4 1.8c.9 2 2.5 3.6 4.5 4.5l1.8-1.4 2.6 2.5-1.6 2.5C6.5 13.7 2.3 9.5 1 4.1z"/></svg>
        </span>
        555-01429-86
      </li>
      <li class="contact-item">
        <span class="contact-icon">
          <svg viewBox="0 0 16 16"><rect x="1.5" y="3.5" width="13" height="9" fill="#fff"/><path d="M1.5 3.5L8 9l6.5-5.5" fill="none" stroke="#6cb33f" stroke-width="1.4"/></svg>
        </span>
        dov@quizwell-demo.net
      </li>
      <li class="contact-item">
        <span class="contact-icon">
          <svg viewBox="0 0 16 16"><path fill="#fff" d="M8 1a5 5 0 0 0-5 5c0 3.6 5 9 5 9s5-5.4 5-9a5 5 0 0 0-5-5z"/><circle cx="8" cy="6" r="1.8" fill="#6cb33f"/></svg>
        </span>
        Your Street address text here City with post code, Country
      </li>
    </ul>
  </section>

  <section class="card card-back" aria-label="Card back">
    <div class="back-lockup">
      <div class="wordmark">Quizwell</div>
      <p class="slogan">Exam Management Made Easy</p>
      <p class="website">www.quizwell-demo.net</p>
    </div>
  </section>
</main>
</body>
</html>
```